Education Certificate

We need a modern yet professional Certificate for those who successfully pass / complete our online Training course.

There are various courses but ONE certificate design required.

the certificate needs to look extremely professional and of value.

```html
<!DOCTYPE html>
<html lang="en">
<head>
<meta charset="utf-8">
<title>Certificate of Appreciation</title>
<link rel="stylesheet" href="https://fonts.googleapis.com/css2?family=Cormorant+Garamond:wght@500;600&family=Great+Vibes&family=Libre+Baskerville&display=swap">
<style>
  :root {
    --frame-black: #1b1b1b;
    --paper: #ffffff;
    --gold: #b8874a;
    --gold-soft: rgba(190, 145, 80, 0.22);
    --bloom-grey: rgba(200, 200, 200, 0.38);
    --ink: #3a3a3a;
    --ink-dark: #1e1e1e;
  }
  * { margin: 0; padding: 0; box-sizing: border-box; }
  html, body {
    width: 1200px;
    height: 799px;
    overflow: hidden;
    background: var(--frame-black);
  }
  .certificate {
    position: relative;
    width: 1200px;
    height: 799px;
  }
  .certificate__border {
    position: absolute;
    inset: 0;
  }
  .bloom, .flourish {
    position: absolute;
  }
  .bloom--top-right {
    left: 815px; top: 31px; width: 350px; height: 172px;
    background: radial-gradient(ellipse at 55% 45%, var(--bloom-grey) 0%, rgba(200,200,200,0) 70%);
  }
  .bloom--bottom-left {
    left: 40px; top: 468px; width: 425px; height: 300px;
    background: radial-gradient(ellipse at 45% 60%, var(--bloom-grey) 0%, rgba(200,200,200,0) 70%);
  }
  .flourish--top-left {
    left: 51px; top: 41px; width: 430px; height: 376px;
    background: radial-gradient(ellipse at 20% 20%, var(--gold-soft) 0%, rgba(190,145,80,0) 62%);
  }
  .flourish--bottom-right {
    left: 718px; top: 351px; width: 433px; height: 407px;
    background: radial-gradient(ellipse at 80% 80%, var(--gold-soft) 0%, rgba(190,145,80,0) 62%);
  }
  .certificate__inner-frame {
    position: absolute;
    left: 124px; top: 113px; width: 952px; height: 574px;
    border: 1.5px solid var(--gold);
  }
  .certificate__content {
    position: absolute;
    left: 0; top: 0; width: 1200px; height: 799px;
    text-align: center;
  }
  .title {
    position: absolute;
    top: 200px; left: 0; width: 1200px;
    font-family: "Cormorant Garamond", serif;
    font-weight: 600;
    font-size: 52px;
    letter-spacing: 9px;
    color: var(--ink);
    line-height: 1;
  }
  .subtitle-row {
    position: absolute;
    top: 254px; left: 0; width: 1200px;
    display: flex; justify-content: center; align-items: center; gap: 32px;
  }
  .subtitle-row__rule {
    width: 76px; height: 3px;
    background: var(--gold);
    border-radius: 50%;
  }
  .subtitle {
    font-family: "Cormorant Garamond", serif;
    font-weight: 600;
    font-size: 27px;
    letter-spacing: 2.5px;
    color: var(--gold);
    line-height: 1;
  }
  .presented {
    position: absolute;
    top: 309px; left: 0; width: 1200px;
    font-family: "Libre Baskerville", serif;
    font-size: 11px;
    letter-spacing: 1px;
    color: var(--ink);
  }
  .recipient {
    position: absolute;
    top: 352px; left: 0; width: 1200px;
    font-family: "Great Vibes", cursive;
    font-size: 54px;
    color: var(--ink-dark);
    line-height: 1;
  }
  .dotted {
    position: absolute;
    height: 3px;
    background-image: radial-gradient(circle, var(--ink-dark) 1.4px, transparent 1.6px);
    background-size: 14px 3px;
  }
  .dotted--name { top: 424px; left: 391px; width: 413px; }
  .description {
    position: absolute;
    top: 454px; left: 320px; width: 560px;
    font-family: "Libre Baskerville", serif;
    font-size: 9.5px;
    line-height: 18px;
    letter-spacing: 0.6px;
    color: var(--ink-dark);
  }
  .field {
    position: absolute;
    top: 560px;
    text-align: center;
  }
  .field--date { left: 395px; width: 142px; }
  .field--signature { left: 645px; width: 210px; }
  .field .dotted { position: static; width: 100%; }
  .field__label {
    margin-top: 12px;
    font-family: "Libre Baskerville", serif;
    font-size: 16px;
    letter-spacing: 2px;
    color: var(--ink);
  }
</style>
</head>
<body>
  <main class="certificate">
    <svg class="certificate__border" width="1200" height="799" viewBox="0 0 1200 799" aria-hidden="true">
      <path d="M52 30 H1148 A20 20 0 0 0 1168 50 V749 A20 20 0 0 0 1148 769 H52 A20 20 0 0 0 32 749 V50 A20 20 0 0 0 52 30 Z"
            fill="var(--paper)" stroke="var(--gold)" stroke-width="3"/>
    </svg>

    <div class="bloom bloom--top-right" role="img" aria-label="Faint grey line-drawn flower in the background"></div>
    <div class="bloom bloom--bottom-left" role="img" aria-label="Faint grey line-drawn flower in the background"></div>

    <div class="certificate__inner-frame"></div>

    <div class="flourish flourish--top-left" role="img" aria-label="Gold baroque scroll ornament in the top left corner"></div>
    <div class="flourish flourish--bottom-right" role="img" aria-label="Gold baroque scroll ornament in the bottom right corner"></div>

    <section class="certificate__content">
      <h1 class="title">CERTIFICATE</h1>
      <div class="subtitle-row">
        <span class="subtitle-row__rule"></span>
        <h2 class="subtitle">OF APPRECIATION</h2>
        <span class="subtitle-row__rule"></span>
      </div>
      <p class="presented">THIS CERTIFICATE IS PROUDLY PRESENTED TO</p>
      <p class="recipient">Eleanor Whitfield</p>
      <div class="dotted dotted--name"></div>
      <p class="description">LOREM IPSUM DOLOR SIT AMET, CONSECTETUER ADIPISCING ELIT, SED DIAM NONUMMY NIBH EUISMOD TINCIDUNT UT LAOREET DOLORE MAGNA ALIQUAM ERAT VOLUTPAT.</p>

      <div class="field field--date">
        <div class="dotted"></div>
        <p class="field__label">DATE</p>
      </div>
      <div class="field field--signature">
        <div class="dotted"></div>
        <p class="field__label">SIGNATURE</p>
      </div>
    </section>
  </main>
</body>
</html>
```